Graduation Day Sale Banner Ad for Website

We need a banner for our upscale jewelry website. Banner must have a classy high end look. The size of the banner must be 1187 × 400. I have attached pieces we would like used (some or all). The banner is for a Graduation Day sale that we are running. The banner should say "Graduation Day Gifts on Sale"

Target Market(s)

Wealthy individuals looking to buy graduation gifts for their children

Industry/Entity Type

Jewelry

Requirements
Must have
• Must match the look and feel of the website (www.fenlustre.com)

```html
<!DOCTYPE html>
<html lang="en">
<head>
<meta charset="utf-8">
<title>Graduation Day Gifts on Sale – Banner</title>
<link rel="stylesheet" href="https://fonts.googleapis.com/css2?family=Leckerli+One&display=swap">
<style>
  :root {
    --page-bg: #3a4044;
    --banner-red: #e8160a;
    --banner-orange: #f25a10;
    --banner-deep: #c42a05;
    --band-dark: #5a1404;
    --ring-outer: #f6c6b8;
    --ring-dark: #4a1a0c;
    --disc-white: #ffffff;
    --title-white: #ffffff;
    --photo-warm: #c9772e;
    --photo-dark: #5a3320;
    --gold: #d9ad4a;
    --gold-deep: #b5862c;
    --silver: #d6d9de;
    --silver-deep: #a9aeb6;
    --garnet: #9a4a62;
  }
  * { box-sizing: border-box; margin: 0; padding: 0; }
  html, body {
    width: 1200px; height: 1200px; overflow: hidden;
    background: var(--page-bg);
  }
  .canvas {
    position: relative; width: 1200px; height: 1200px;
    display: flex; align-items: center; justify-content: center;
  }
  .banner {
    position: relative; width: 1187px; height: 400px; overflow: hidden;
    background:
      radial-gradient(circle at 300px 120px, rgba(255,120,80,0.35), transparent 160px),
      radial-gradient(circle at 700px 90px, rgba(255,140,90,0.3), transparent 140px),
      radial-gradient(circle at 560px 330px, rgba(255,150,60,0.3), transparent 150px),
      linear-gradient(180deg, var(--banner-red) 0%, var(--banner-orange) 60%, var(--banner-deep) 100%);
  }
  .banner__model {
    position: absolute; right: 0; top: 0; width: 300px; height: 400px;
    background: linear-gradient(90deg, rgba(201,119,46,0) 0%, var(--photo-warm) 22%, var(--photo-dark) 60%, var(--photo-warm) 100%);
    z-index: 1;
  }
  .banner__title {
    position: absolute; left: 42px; top: 50px; z-index: 3;
    font-family: "Leckerli One", cursive;
    font-size: 58px; line-height: 1; letter-spacing: 0.3px;
    color: var(--title-white);
    text-shadow: 0 3px 4px rgba(90,20,0,0.55);
    white-space: nowrap;
  }
  .banner__band {
    position: absolute; left: 0; bottom: 0; width: 880px; height: 24px; z-index: 2;
    background: linear-gradient(90deg, var(--band-dark) 0%, var(--band-dark) 80%, rgba(90,20,4,0) 100%);
  }
  .product {
    position: absolute; border-radius: 50%; z-index: 2;
    background: var(--ring-outer);
    box-shadow: 0 4px 10px rgba(80,10,0,0.45);
  }
  .product__ring { position: absolute; inset: 6px; border-radius: 50%; background: var(--ring-dark); }
  .product__disc { position: absolute; inset: 12px; border-radius: 50%; background: var(--disc-white); }
  .product__item { position: absolute; left: 24%; right: 24%; top: 30%; bottom: 30%; border-radius: 10px; }
  .product--small { width: 160px; height: 160px; }
  .product--large { width: 194px; height: 194px; }
  .product--pearl-ring { left: 65px; top: 172px; }
  .product--band-ring { left: 240px; top: 155px; }
  .product--heart-pendant { left: 444px; top: 155px; }
  .product--drop-earrings { left: 655px; top: 172px; }
  .item--gold { background: linear-gradient(180deg, var(--gold), var(--gold-deep)); }
  .item--silver { top: 22%; bottom: 22%; background: linear-gradient(180deg, var(--silver), var(--silver-deep)); }
  .item--earring { background: linear-gradient(180deg, var(--gold), var(--garnet)); }
</style>
</head>
<body>
<main class="canvas">
  <section class="banner">
    <div class="banner__model" role="img" aria-label="Photo of a woman wearing gold jewelry against warm bokeh lights"></div>

    <h1 class="banner__title">Graduation Day Gifts on Sale</h1>

    <div class="product product--small product--pearl-ring">
      <div class="product__ring"></div>
      <div class="product__disc"></div>
      <div class="product__item item--gold" role="img" aria-label="Gold ring with pearls and diamonds"></div>
    </div>
    <div class="product product--large product--band-ring">
      <div class="product__ring"></div>
      <div class="product__disc"></div>
      <div class="product__item item--gold" role="img" aria-label="Gold and white gold band ring"></div>
    </div>
    <div class="product product--large product--heart-pendant">
      <div class="product__ring"></div>
      <div class="product__disc"></div>
      <div class="product__item item--silver" role="img" aria-label="Diamond heart pendant with sapphires on a chain"></div>
    </div>
    <div class="product product--small product--drop-earrings">
      <div class="product__ring"></div>
      <div class="product__disc"></div>
      <div class="product__item item--earring" role="img" aria-label="Pair of gold drop earrings with pink stones"></div>
    </div>

    <div class="banner__band"></div>
  </section>
</main>
</body>
</html>
```